Business card for boutique investment firm

Need a business card designed for our boutique investment firm called "BrightLedger Investment Fee Advisors". We help investors achieve lower fees through negotiation on their behalf. We have a logo to work with and a color palette. The card should incorporate our tag line "Clear fees, lasting gains" and space for relevant details. The look and feel should reflect the logo and our brand personality: Humble, Trustworthy, Friendly

Target Market(s)

High net worth investors who are looking for clarity around how they are being charged by their investment advisor

Industry/Entity Type

Boutique

Requirements
Must have
• Logo
Tag line: Clear fees, lasting gains
Space for relevant contact details: name, title, phone, email, URL, mailing address

Use these fonts: 'AvantGarde Bk BT' and 'AvantGarde Bk BT Demi'
Use these colors:
Orange = C-0 / M-60 / Y-100 / K-0
Grey = C-0 / M-0 / Y-0 / K-60

```html
<!DOCTYPE html>
<html lang="en">
<head>
<meta charset="UTF-8">
<title>BrightLedger – Business Card</title>
<link rel="stylesheet" href="https://fonts.googleapis.com/css2?family=Questrial&display=swap">
<style>
  :root {
    --orange: #f47b20;
    --orange-deep: #d9661a;
    --orange-light: #f7913a;
    --grey: #808285;
    --grey-dark: #4d4d4f;
    --paper: #f4f4f4;
    --paper-shade: #dcdcdc;
    --backdrop: #222222;
    --white: #ffffff;
  }
  * { margin: 0; padding: 0; box-sizing: border-box; }
  html, body {
    width: 1200px;
    height: 904px;
    overflow: hidden;
    background: var(--backdrop);
    font-family: 'Questrial', 'Century Gothic', sans-serif;
  }
  .stage { position: relative; width: 1200px; height: 904px; }
  .card { position: absolute; width: 520px; height: 300px; overflow: hidden; }
  .card__wave { position: absolute; inset: 0; width: 100%; height: 100%; }

  /* Front */
  .card--front {
    left: 150px;
    top: 170px;
    background: radial-gradient(ellipse at 38% 35%, var(--orange-light) 0%, var(--orange) 45%, var(--orange-deep) 100%);
  }
  .brand { position: absolute; display: flex; align-items: center; }
  .brand__mark { border-radius: 50%; flex: none; }
  .brand__text { display: flex; flex-direction: column; }
  .brand__name { line-height: 1; letter-spacing: -0.5px; white-space: nowrap; }
  .brand__sub { line-height: 1.15; letter-spacing: 0.5px; white-space: nowrap; }
  .brand__tagline { line-height: 1.2; white-space: nowrap; }

  .card--front .brand { left: 95px; top: 108px; }
  .card--front .brand__mark {
    width: 62px; height: 62px;
    border: 6px solid var(--white);
    margin-right: 12px;
  }
  .card--front .brand__name { font-size: 40px; color: var(--white); }
  .card--front .brand__sub { font-size: 15px; color: var(--white); }
  .card--front .brand__tagline { font-size: 15px; color: var(--white); }

  /* Back */
  .card--back {
    left: 530px;
    top: 490px;
    background: linear-gradient(180deg, var(--paper-shade) 0%, var(--paper) 55%, var(--white) 100%);
  }
  .card--back .brand { left: 28px; top: 118px; }
  .card--back .brand__mark {
    width: 38px; height: 38px;
    border: 4px solid var(--orange);
    margin-right: 8px;
  }
  .card--back .brand__name { font-size: 24px; color: var(--orange); }
  .card--back .brand__sub { font-size: 9px; color: var(--grey); }
  .card--back .brand__tagline { font-size: 9px; color: var(--grey-dark); }

  .divider {
    position: absolute;
    left: 262px;
    top: 78px;
    height: 126px;
    border-left: 2px dashed var(--orange);
  }
  .contact { position: absolute; left: 282px; top: 96px; color: var(--grey-dark); }
  .contact__name { font-size: 14px; color: var(--grey-dark); }
  .contact__title { font-size: 13px; color: var(--grey); margin-bottom: 6px; }
  .contact__line { font-size: 10px; line-height: 1.75; }
  .web {
    position: absolute;
    left: 0; right: 0;
    bottom: 24px;
    text-align: center;
    font-size: 12px;
    color: var(--grey-dark);
  }
  .web__sep { color: var(--grey); margin: 0 6px; }
</style>
</head>
<body>
<main class="stage">
  <section class="card card--front" aria-label="Card front">
    <svg class="card__wave" viewBox="0 0 520 300" preserveAspectRatio="none" aria-hidden="true">
      <path d="M0 250 C 150 180, 300 240, 420 170 C 470 140, 500 80, 520 40 L520 300 L0 300 Z" fill="#e06e1c" opacity="0.55"/>
      <path d="M0 270 C 160 220, 320 260, 520 190" stroke="#f89a4a" stroke-width="1.5" fill="none" opacity="0.6"/>
    </svg>
    <div class="brand">
      <span class="brand__mark"></span>
      <div class="brand__text">
        <span class="brand__name">BrightLedger</span>
        <span class="brand__sub">Fee Clarity Partners</span>
        <span class="brand__tagline">Clear fees, lasting gains</span>
      </div>
    </div>
  </section>

  <section class="card card--back" aria-label="Card back">
    <svg class="card__wave" viewBox="0 0 520 300" preserveAspectRatio="none" aria-hidden="true">
      <path d="M0 190 C 140 215, 260 190, 360 130 C 420 95, 480 85, 520 90 L520 300 L0 300 Z" fill="#ffffff" opacity="0.85"/>
    </svg>
    <div class="brand">
      <span class="brand__mark"></span>
      <div class="brand__text">
        <span class="brand__name">BrightLedger</span>
        <span class="brand__sub">Fee Clarity Partners</span>
        <span class="brand__tagline">Clear fees, lasting gains</span>
      </div>
    </div>
    <div class="divider"></div>
    <div class="contact">
      <p class="contact__name">Name</p>
      <p class="contact__title">Title</p>
      <p class="contact__line">Adress line 1</p>
      <p class="contact__line">Adress line ........2</p>
      <p class="contact__line">Contact : +41 555 01 23</p>
    </div>
    <p class="web">www.brightledger-advisors.com<span class="web__sep">|</span>mail@brightledger-advisors.com</p>
  </section>
</main>
</body>
</html>
```